Online Nutrition Consulting Website/healthy lifestyle

This is a website for online nutrition consulting. (For example, weight loss.) The company is called Mirela's. I included the logo so you have a feel for the colors and the message of the company. I would like to have one main neutral color in there. (I am leaning toward grey, but I am open to ideas) I would like the design to be simple and to the point.

My ultimate goal is for my website to stand out from other nutrition websites by projecting my slogan (It's not a diet. It's a lifestyle.)

Target Market(s)

Health-conscious people.

Industry/Entity Type

Nutrition

Coding

Coded - Design and coding required

Number of Pages Required

4 page

Font styles to use
Script

Requirements
Must have
• Home page, Services page , About page, and a Blog page. (Once I see the layout, I will give you more detail so it isn't confusing. For example: payment of services and the "About me")
• Logo must be included.
• Easy navigation. Not too much scrolling.

```html
<!DOCTYPE html>
<html lang="en">
<head>
<meta charset="utf-8">
<title>Mirela's – Nutrition Consulting</title>
<link href="https://fonts.googleapis.com/css2?family=Josefin+Sans:wght@300;400;600&family=Open+Sans:wght@400;600&display=swap" rel="stylesheet">
<style>
:root{
  --blue:#1ba8e0;
  --blue-dark:#0d86bf;
  --blue-deep:#0a6a99;
  --green:#8cc63f;
  --white:#ffffff;
  --text:#555b61;
  --light:#eef3f6;
}
*{box-sizing:border-box;margin:0;padding:0}
html,body{width:710px;height:1200px;overflow:hidden;background:var(--white)}
body{position:relative;font-family:"Open Sans",sans-serif;color:var(--text)}
.abs{position:absolute}
.heading{font-family:"Josefin Sans",sans-serif;font-weight:300;letter-spacing:1px}
.body-copy{font-size:9.5px;line-height:14px}
.btn{display:inline-block;background:var(--white);color:var(--blue-dark);font-size:8.5px;padding:4px 10px;border:1px solid var(--white)}

/* header */
.site-header{left:0;top:0;width:710px;height:92px}
.logo{left:38px;top:22px;display:flex;align-items:center;gap:8px}
.logo-dot{width:26px;height:26px;border-radius:50%;background:var(--green)}
.logo-name{font-family:"Josefin Sans",sans-serif;font-weight:600;font-size:30px;color:var(--blue-dark)}
.nav{right:20px;top:34px;display:flex;gap:20px;font-family:"Josefin Sans",sans-serif;font-size:14px;color:var(--blue)}
.nav .active{color:var(--green)}

/* hero */
.hero{left:0;top:95px;width:710px;height:280px}
.hero-title{left:0;top:22px;width:520px;text-align:center;color:var(--white);font-size:30px}
.hero-rule{left:290px;top:66px;width:110px;height:2px;background:var(--green)}
.hero-copy{left:45px;top:100px;width:230px;color:var(--white)}
.hero-btn{left:120px;top:232px}

/* services */
.section-title{width:710px;text-align:center;font-size:30px;color:var(--blue)}
.section-title .accent{color:var(--blue-dark)}
.service-title{font-family:"Josefin Sans",sans-serif;font-size:16px;color:var(--white)}
.service-copy{color:var(--white);width:250px}

/* testimonials */
.quote-arrow{font-size:30px;color:var(--blue-deep);font-family:"Josefin Sans",sans-serif}

/* footer */
.footer{left:0;top:950px;width:710px;height:210px}
.footer-title{font-size:18px;color:var(--white)}
.blog-item{display:flex;gap:10px;color:var(--white);width:290px}
.thumb{width:44px;height:44px;flex:none}
.field{background:var(--white);border:1px solid #cfe3ee;font-size:8.5px;color:#8a9aa4;padding:3px 6px;width:260px}
.submit{background:var(--white);color:var(--blue-dark);font-size:8.5px;padding:4px 12px}
.bottom-bar{left:0;top:1160px;width:710px;height:40px;background:var(--blue-deep)}
.copyright{left:40px;top:14px;font-size:8px;color:var(--white)}
.social{right:40px;top:10px;display:flex;gap:12px}
.social span{width:20px;height:20px;border-radius:50%;background:var(--white)}
</style>
</head>
<body>

<header class="abs site-header">
  <div class="abs logo"><span class="logo-dot"></span><span class="logo-name">Mirela's</span></div>
  <nav class="abs nav">
    <span class="active">HOME</span><span>ABOUT US</span><span>SERVICES</span><span>BLOG</span><span>CONTACT US</span>
  </nav>
</header>

<section class="abs hero">
  <svg class="abs" style="left:0;top:0" width="710" height="280">
    <defs>
      <linearGradient id="heroPhoto" x1="0" y1="0" x2="1" y2="1">
        <stop offset="0" stop-color="#f4f4f4"/><stop offset="1" stop-color="#e3d6cf"/>
      </linearGradient>
    </defs>
    <rect x="400" y="0" width="310" height="280" fill="url(#heroPhoto)" role="img" aria-label="Smiling woman holding a water bottle and a green apple"/>
    <polygon points="0,0 520,0 440,280 0,280" fill="var(--blue)"/>
  </svg>
  <h1 class="abs heading hero-title">WELCOME TO MIRELA'S</h1>
  <div class="abs hero-rule"></div>
  <p class="abs body-copy hero-copy">Lorem Ipsum is simply dummy text of the printing and typesetting industry. Lorem Ipsum has been the industry's standard dummy text ever since the 1500s, when an unknown printer took a galley of type and scrambled it to make a type specimen book. It has survived not only five centuries, but also the leap into electronic typesetting, remaining essentially unchanged.</p>
  <span class="abs btn hero-btn">Read More</span>
</section>

<h2 class="abs heading section-title" style="left:0;top:392px">OUR <span class="accent">SERVICES</span></h2>

<section class="abs" style="left:0;top:440px;width:710px;height:318px">
  <svg class="abs" style="left:0;top:0" width="710" height="318">
    <defs>
      <linearGradient id="fruitPhoto" x1="0" y1="0" x2="1" y2="1">
        <stop offset="0" stop-color="#f6d27a"/><stop offset="1" stop-color="#e06a3c"/>
      </linearGradient>
      <linearGradient id="waistPhoto" x1="0" y1="0" x2="1" y2="1">
        <stop offset="0" stop-color="#f3ece7"/><stop offset="1" stop-color="#d9c2b3"/>
      </linearGradient>
    </defs>
    <rect x="0" y="0" width="320" height="160" fill="#ffffff"/>
    <rect x="40" y="15" width="260" height="140" fill="url(#fruitPhoto)" role="img" aria-label="Woman with a spread of fresh fruit"/>
    <polygon points="340,0 710,0 710,160 290,160" fill="var(--blue)"/>
    <rect x="400" y="160" width="310" height="158" fill="url(#waistPhoto)" role="img" aria-label="Slim waist with a measuring tape"/>
    <polygon points="0,160 470,160 420,295 0,295" fill="var(--blue)"/>
  </svg>
  <h3 class="abs service-title" style="left:385px;top:24px">DIET PLANNING</h3>
  <p class="abs body-copy service-copy" style="left:385px;top:50px">Lorem Ipsum is simply dummy text of the printing and typesetting industry. Lorem Ipsum has been the industry's standard dummy text ever since the 1500s, when an unknown printer took a galley.</p>
  <span class="abs btn" style="left:385px;top:115px">Read More</span>
  <h3 class="abs service-title" style="left:110px;top:180px">WEIGHT MANAGEMENT</h3>
  <p class="abs body-copy service-copy" style="left:45px;top:205px;width:280px;text-align:center">Lorem Ipsum is simply dummy text of the printing and typesetting industry. Lorem Ipsum has been the industry's standard dummy text ever since the 1500s, when an unknown printer took a galley.</p>
  <span class="abs btn" style="left:265px;top:262px">Read More</span>
</section>

<h2 class="abs heading section-title" style="left:0;top:772px">TESTIMONIALS</h2>
<section class="abs" style="left:0;top:815px;width:710px;height:120px">
  <span class="abs quote-arrow" style="left:45px;top:38px">«</span>
  <svg class="abs" style="left:122px;top:10px" width="90" height="90">
    <rect width="90" height="90" fill="#e9c3a8" role="img" aria-label="Portrait of a happy client"/>
  </svg>
  <p class="abs body-copy" style="left:240px;top:30px;width:400px">Lorem Ipsum is simply dummy text of the printing and typesetting industry. Lorem Ipsum has been the industry's standard dummy text ever since the 1500s, when an unknown printer took a galley of type.</p>
  <span class="abs quote-arrow" style="left:645px;top:38px">»</span>
</section>

<footer class="abs footer">
  <svg class="abs" style="left:0;top:0" width="710" height="210">
    <defs>
      <linearGradient id="footerBg" x1="0" y1="0" x2="1" y2="1">
        <stop offset="0" stop-color="#2eb3e6"/><stop offset="1" stop-color="#1590c9"/>
      </linearGradient>
    </defs>
    <rect width="710" height="210" fill="url(#footerBg)" role="img" aria-label="Soft blue background of healthy food imagery"/>
  </svg>
  <h3 class="abs heading footer-title" style="left:160px;top:25px">BLOG</h3>
  <div class="abs blog-item" style="left:45px;top:65px">
    <svg class="thumb"><rect width="44" height="44" fill="#e6c9b4" role="img" aria-label="Blog post thumbnail"/></svg>
    <p class="body-copy">Lorem Ipsum is simply dummy text of the printing and typesetting industry. Lorem Ipsum has been the industry's standard.</p>
  </div>
  <div class="abs blog-item" style="left:45px;top:125px">
    <svg class="thumb"><rect width="44" height="44" fill="#d9cbc2" role="img" aria-label="Blog post thumbnail"/></svg>
    <p class="body-copy">Lorem Ipsum is simply dummy text of the printing and typesetting industry. Lorem Ipsum has been the industry's standard.</p>
  </div>
  <h3 class="abs heading footer-title" style="left:455px;top:25px">CONTACT US</h3>
  <div class="abs field" style="left:380px;top:66px">Name</div>
  <div class="abs field" style="left:380px;top:88px;height:44px">Email</div>
  <span class="abs submit" style="left:380px;top:140px">Submit</span>
</footer>

<div class="abs bottom-bar">
  <span class="abs copyright">Copyright © 2015 All Rights Reserved</span>
  <div class="abs social"><span></span><span></span><span></span></div>
</div>

</body>
</html>
```